BRIARWOOD LOUNGE FRIDAY MAY 3

Flyer design for bar/nightclub event. Trying to keep a general theme with their flyers (see below) but would like to add some neon or some pop to it.

TEXT:

Briarwood Bar & Lounge Presents

LANTERN NIGHTS
GRAND OPENING EVENT

PURE HOUSE MUSIC W/

VORTEX
MARCO TELLEN
BRANDT & DJ WOBNIX

21+
9PM-130AM
712 K AVENUE DAVIS CA

Target Market(s)

House/dance music crowd.

Industry/Entity Type

Night Club

Font styles to use
Sans Serif

Colors
9bcb3c
fbee3d
ffffff

Requirements
Must have
• Large DJ names
Nice to have
• General theme of the attached flyers. Neon colors that stick with the theme. Anything else that looks cool will be considered

```html
<!DOCTYPE html>
<html lang="en">
<head>
<meta charset="utf-8">
<title>Briarwood Bar &amp; Lounge – Lantern Nights Grand Opening</title>
<link rel="stylesheet" href="https://fonts.googleapis.com/css2?family=Montserrat:wght@600;700;800;900&display=swap">
<style>
  :root {
    --flame-light: #f6c63a;
    --flame-mid: #eaa823;
    --flame-deep: #d98a17;
    --bark: #3d2f29;
    --pine: #3a5441;
    --gold: #e8b530;
    --cream: #ece5cf;
    --ember: #f08a1c;
  }
  * { margin: 0; padding: 0; box-sizing: border-box; }
  html, body {
    width: 857px; height: 1200px; overflow: hidden;
    background: var(--bark);
  }
  .flyer {
    position: relative;
    width: 857px; height: 1200px;
    overflow: hidden;
    font-family: "Montserrat", sans-serif;
    color: var(--bark);
    text-align: center;
  }
  .flame-backdrop {
    position: absolute; inset: 5px;
    background:
      radial-gradient(ellipse at 30% 40%, rgba(255,220,90,.55), transparent 60%),
      radial-gradient(ellipse at 75% 75%, rgba(255,210,80,.45), transparent 55%),
      linear-gradient(170deg, var(--flame-light) 0%, var(--flame-mid) 55%, var(--flame-deep) 100%);
  }
  .logo-frame {
    position: absolute; left: 131px; top: 45px; width: 597px; height: 175px;
    background: var(--gold);
  }
  .logo-square {
    position: absolute; left: 138px; top: 52px; width: 160px; height: 161px;
    background: var(--pine);
  }
  .logo-name {
    position: absolute; left: 306px; top: 52px; width: 416px; height: 161px;
    background: var(--bark);
    color: var(--cream);
    font-weight: 800;
    display: flex; flex-direction: column; align-items: center; justify-content: center;
    line-height: 1;
  }
  .logo-name .venue { font-size: 52px; letter-spacing: 1px; }
  .logo-name .venue-type { font-size: 24px; margin-top: 10px; }
  .logo-name .venue-city { font-size: 12px; margin-top: 8px; letter-spacing: 2px; }

  .headline { position: absolute; left: 0; width: 857px; line-height: 1; font-weight: 800; }
  .grand-opening { top: 288px; font-size: 38px; letter-spacing: 6px; }
  .event-title { top: 330px; font-size: 104px; color: var(--pine); font-weight: 900; letter-spacing: 2px; }
  .event-title span { display: block; }
  .event-title .second { margin-top: -8px; letter-spacing: 8px; }
  .music-line { top: 524px; font-size: 32px; letter-spacing: 2px; line-height: 1.1; }

  .campfire {
    position: absolute; top: 470px; width: 210px; height: 125px;
    border-radius: 50% 50% 45% 45%;
    background: radial-gradient(ellipse at 50% 40%, #ffd86a 0%, var(--ember) 35%, #7a4a2c 70%, rgba(90,60,40,0) 100%);
  }
  .campfire.left { left: 10px; }
  .campfire.right { left: 636px; }

  .dj {
    position: absolute; left: 227px; width: 386px; height: 86px;
    background: var(--bark);
    display: flex; align-items: center; justify-content: center;
    font-weight: 800; color: var(--cream); line-height: 1;
  }
  .dj.headliner { top: 618px; color: var(--gold); font-size: 45px; letter-spacing: 3px; }
  .dj.second { top: 745px; font-size: 36px; letter-spacing: 3px; }
  .dj.third { top: 875px; font-size: 29px; letter-spacing: 2px; }

  .event-date {
    position: absolute; top: 1020px; left: 0; width: 857px;
    font-size: 43px; font-weight: 800; letter-spacing: 2px; line-height: 1;
    color: var(--cream);
  }
  .event-date .dark { color: var(--bark); }
  .event-date sub { font-size: 22px; vertical-align: baseline; }
  .event-hours {
    position: absolute; top: 1080px; left: 0; width: 857px;
    font-size: 31px; font-weight: 800; letter-spacing: 1px;
  }
  .age-corner { position: absolute; right: 0; bottom: 0; }
  .age-limit {
    position: absolute; right: 14px; bottom: 32px;
    font-size: 29px; font-weight: 800; color: var(--cream);
  }
  .location {
    position: absolute; left: 0; bottom: 4px; width: 857px;
    font-size: 24px; font-weight: 700; letter-spacing: 3px; color: var(--cream);
  }
</style>
</head>
<body>
<main class="flyer">
  <div class="flame-backdrop" role="img" aria-label="Background of golden flames and smoke"></div>

  <header>
    <div class="logo-frame"></div>
    <div class="logo-square"></div>
    <div class="logo-name">
      <span class="venue">BRIARWOOD</span>
      <span class="venue-type">BAR &amp; LOUNGE</span>
      <span class="venue-city">DAVIS, CA.</span>
    </div>
  </header>

  <p class="headline grand-opening">GRAND OPENING</p>
  <h1 class="headline event-title"><span>LANTERN</span><span class="second">NIGHTS</span></h1>

  <div class="campfire left" role="img" aria-label="Burning campfire logs"></div>
  <div class="campfire right" role="img" aria-label="Burning campfire logs"></div>

  <p class="headline music-line">HOUSE MUSIC<br>WITH</p>

  <div class="dj headliner">VORTEX</div>
  <div class="dj second">MARCO TELLEN</div>
  <div class="dj third">BRANDT &amp; DJ WOBNIX</div>

  <p class="event-date">FRIDAY<span class="dark">03<sub>RD</sub></span>MAY<span class="dark">2019</span></p>
  <p class="event-hours">FROM 21:00 TO 01:30</p>

  <svg class="age-corner" width="137" height="163" viewBox="0 0 137 163" aria-hidden="true">
    <polygon points="137,0 137,163 0,163" fill="var(--bark)"/>
  </svg>
  <p class="age-limit">21+</p>

  <p class="location">LOCATION: 712 K AVENUE DAVIS CA</p>
</main>
</body>
</html>
```